MotoBrisk flyer design

I need something that is bold and punchy for a new mobile vehicle valet based in Telford, Shropshire with own water and electricity supply. I have aimed for all colours to be blue and yellow and the flyer must show a special summer offer of "FREE TYRE PRESSURE CHECK AND ADJUSTMENT IF REQUIRED WITH EVERY VALET". I aim to make this business as professionally run as possible and the flyers should echo that.

Requirements
Must have
• Company name - MotoBrisk
Slogan - Where perfection is the only option
Special offer - FREE TYRE PRESSURE CHECK AND ADJUSTMENT WITH EVERY VALET.
Image - vehicle being washed
All contact details - www.motobrisk-demo.co.uk
sales@motobrisk-demo.co.uk
07700900318

```html
<!DOCTYPE html>
<html lang="en">
<head>
<meta charset="utf-8">
<title>MotoBrisk Flyer</title>
<link rel="stylesheet" href="https://fonts.googleapis.com/css2?family=Russo+One&family=Lato:wght@400;700;900&family=Oswald:wght@500;600&display=swap">
<style>
  :root {
    --blue: #1b9ad8;
    --blue-dark: #1a6ea3;
    --blue-light: #4fc0ee;
    --yellow: #f7c614;
    --yellow-deep: #f2a81d;
    --grey-top: #d9dcdf;
    --grey-bottom: #f4f5f6;
    --ink: #1c1f24;
    --text: #2a2d33;
    --white: #ffffff;
  }
  * { margin: 0; padding: 0; box-sizing: border-box; }
  html, body { width: 900px; height: 1200px; overflow: hidden; background: #ffffff; }
  .flyer {
    position: relative;
    width: 900px;
    height: 1200px;
    overflow: hidden;
    background: linear-gradient(180deg, var(--grey-top), var(--grey-bottom));
    font-family: "Lato", sans-serif;
  }
  .backdrop { position: absolute; inset: 0; }
  .headline {
    position: absolute;
    left: 0; right: 0; top: 38px;
    text-align: center;
    font-family: "Russo One", sans-serif;
    font-weight: 400;
    line-height: 1;
  }
  .headline-top { display: block; color: var(--white); font-size: 76px; letter-spacing: 1px; text-shadow: 0 2px 4px rgba(0,0,0,0.25); }
  .headline-bottom { display: block; color: var(--ink); font-size: 76px; margin-top: 6px; letter-spacing: 1px; }
  .brand {
    position: absolute;
    left: 42px; top: 522px;
    font-weight: 900;
    font-size: 66px;
    color: var(--ink);
    line-height: 1;
  }
  .offer-list {
    position: absolute;
    left: 24px; top: 750px;
    list-style: none;
  }
  .offer-list li {
    display: flex; align-items: center; gap: 14px;
    font-weight: 900;
    font-size: 38.5px;
    color: var(--blue-dark);
    line-height: 48px;
  }
  .tick { width: 22px; height: 22px; }
  .free-badge {
    position: absolute;
    left: 630px; top: 634px;
    width: 256px; height: 256px;
    border-radius: 50%;
    background: radial-gradient(circle at 50% 40%, var(--blue-light), var(--blue));
    border: 7px solid var(--white);
    box-shadow: 0 6px 14px rgba(0,0,0,0.25);
    text-align: center;
    font-family: "Oswald", sans-serif;
    color: var(--white);
  }
  .free-word { display: block; margin-top: 30px; font-size: 96px; font-weight: 600; color: var(--yellow); line-height: 1; }
  .free-note { display: block; margin-top: 8px; font-size: 27px; font-weight: 500; line-height: 1; }
  .about-tab {
    position: absolute;
    left: 0; top: 877px;
    width: 246px; height: 58px;
    border-radius: 0 29px 29px 0;
    background: linear-gradient(90deg, var(--yellow), var(--yellow-deep));
    padding-left: 26px;
    font-weight: 700;
    font-size: 36px;
    line-height: 58px;
    color: var(--ink);
  }
  .about-text {
    position: absolute;
    left: 26px; top: 960px; width: 862px;
    font-size: 18.6px;
    line-height: 25px;
    color: var(--text);
  }
  .footer-rule { position: absolute; left: 0; right: 0; top: 1110px; height: 8px; background: var(--yellow); }
  .footer {
    position: absolute;
    left: 0; right: 0; top: 1125px; height: 75px;
    background: linear-gradient(180deg, var(--blue-light), var(--blue));
    font-weight: 700; font-size: 20px; color: var(--white);
  }
  .contact { position: absolute; top: 0; height: 75px; display: flex; align-items: center; gap: 8px; }
  .contact-phone { left: 26px; }
  .contact-email { left: 270px; }
  .contact-web { left: 596px; }
  .contact svg { width: 16px; height: 16px; fill: var(--white); }
</style>
</head>
<body>
<div class="flyer">
  <svg class="backdrop" width="900" height="1200" viewBox="0 0 900 1200">
    <defs>
      <linearGradient id="photoTone" x1="0" y1="0" x2="0.5" y2="1">
        <stop offset="0" stop-color="#4f7ea9"/>
        <stop offset="0.5" stop-color="#8fb1cf"/>
        <stop offset="1" stop-color="#d3e1ec"/>
      </linearGradient>
      <radialGradient id="carShade" cx="0.62" cy="0.62" r="0.45">
        <stop offset="0" stop-color="#3c5670" stop-opacity="0.75"/>
        <stop offset="0.6" stop-color="#5d7d9b" stop-opacity="0.35"/>
        <stop offset="1" stop-color="#8fb1cf" stop-opacity="0"/>
      </radialGradient>
      <linearGradient id="waveBlue" x1="0" y1="0" x2="1" y2="0">
        <stop offset="0" stop-color="#2aa3dd"/>
        <stop offset="1" stop-color="#5cc6f0"/>
      </linearGradient>
    </defs>
    <g class="hero-photo" role="img" aria-label="Photo of a car being washed in a spray of water">
      <path fill="url(#photoTone)" d="M0,0 H900 V520 C640,615 520,570 430,430 C330,300 180,215 0,270 Z"/>
      <path fill="url(#carShade)" d="M0,0 H900 V520 C640,615 520,570 430,430 C330,300 180,215 0,270 Z"/>
    </g>
    <path class="wave-yellow" fill="#f7c614"
      d="M0,345 C180,330 330,420 430,540 C510,640 620,680 740,668 C620,722 520,692 420,612 C310,512 170,422 0,442 Z"/>
    <path class="wave-blue" fill="url(#waveBlue)"
      d="M0,270 C180,215 330,300 430,430 C520,570 640,615 900,520 V585 C660,700 520,655 430,540 C330,420 180,330 0,345 Z"/>
  </svg>

  <h1 class="headline">
    <span class="headline-top">Where Perfection is</span>
    <span class="headline-bottom">THE ONLY OPTION</span>
  </h1>

  <div class="brand">MotoBrisk</div>

  <ul class="offer-list">
    <li><svg class="tick" viewBox="0 0 24 24"><path d="M3 13 L9 19 L21 5" fill="none" stroke="#1a6ea3" stroke-width="4" stroke-linecap="round" stroke-linejoin="round"/></svg>TYRE PRESSURE CHECK</li>
    <li><svg class="tick" viewBox="0 0 24 24"><path d="M3 13 L9 19 L21 5" fill="none" stroke="#1a6ea3" stroke-width="4" stroke-linecap="round" stroke-linejoin="round"/></svg>TYRE PRESSURE ADJUSTMENT</li>
  </ul>

  <div class="free-badge">
    <span class="free-word">FREE</span>
    <span class="free-note">WITH EVERY VALET</span>
  </div>

  <h2 class="about-tab">About Us</h2>
  <p class="about-text">MotoBrisk is focused on providing high-quality service and customer satisfaction in full vehicle valeting - we will do everything we can to meet your expectations. From mini valets to full valets MotoBrisk is an independent company which only uses the top of the range car cleaning products and are completely mobile, with own water and electricity supply meaning your vehicle can be fitted in around your busy lifestyle whether it be at home, work or maybe just out for the day.</p>

  <div class="footer-rule"></div>
  <footer class="footer">
    <span class="contact contact-phone"><svg viewBox="0 0 24 24"><path d="M6.6 10.8c1.4 2.8 3.8 5.1 6.6 6.6l2.2-2.2c.3-.3.7-.4 1-.2 1.1.4 2.3.6 3.6.6.6 0 1 .4 1 1V20c0 .6-.4 1-1 1C10.6 21 3 13.4 3 4c0-.6.4-1 1-1h3.5c.6 0 1 .4 1 1 0 1.3.2 2.5.6 3.6.1.3 0 .7-.2 1z"/></svg>07700900318</span>
    <span class="contact contact-email"><svg viewBox="0 0 24 24"><path d="M2 5h20v14H2z M2 5l10 8 10-8" fill="#fff" stroke="#1b9ad8" stroke-width="1.5"/></svg>sales@motobrisk-demo.co.uk</span>
    <span class="contact contact-web"><svg viewBox="0 0 24 24"><circle cx="12" cy="12" r="10"/><path d="M2 12h20M12 2c3 3 3 17 0 20M12 2c-3 3-3 17 0 20" fill="none" stroke="#1b9ad8" stroke-width="1.5"/></svg>www.motobrisk-demo.co.uk</span>
  </footer>
</div>
</body>
</html>
```